Makeup Brush Cover Labeling/Packaging

Launching a new brush cover product that is designed to cover the bristles of various sized makeup brushes to protect them from grime and debris. We are a small company that is looking to grow and this would be an excellent opportunity to grow with us! Our current website is: thelashmitten.com, but the updated version is to be released in December, 2013.

I am looking for packaging and labeling designs to show off the uniqueness of the PlumeSleeve. I am currently considering strong transparent sleeves with heat sealed edges and want the product to do the selling itself (aka it's important that the customer can see the product right away! and understand its use) but am not opposed to boxes, cylinders, pillow-shaped packaging, etc. The sky is the limit. The final design should feel sophisticated and creative, and should give the feel of 'luxury' as it is a luxury product.

The product comes in three sizes, see attachment for an idea of size mockup.

The final label design could be simple, picture a basic insert in a transparent sleeve (sleeve not pictured, just simple label), inspiration: http://themaplekettlejournal.examplepress.com/2009/07/23/no-1/)

or it could be complex in color, font and style (I love the bold text, black background and color splashes here!), inspiration: http://www.boxmuseboard.com/vantel-q-for-lorvane.html/#!prettyPhoto/1/

Also attaching a simple box with transparent window idea (if we go box, we'll have the window be most of the front of the packaging).

Reason: I really appreciate everyone's designs! I would like to see if this project can attract anymore to review. At this time I'm looking for a label and packaging and most designs are packaging only.

Target Market(s)

Women 20+, women who would purchase luxury 'add-on' items for their makeup kits. This should be a design you can picture placed in a Lorvane or Marko store.

Industry/Entity Type

It Company

Font styles to use
Sans Serif

Requirements
Must have
• Should be both a labeling and packaging idea.

```html
<!DOCTYPE html>
<html lang="en">
<head>
<meta charset="utf-8">
<title>PlumeSleeve Packaging Range</title>
<link rel="stylesheet" href="https://fonts.googleapis.com/css2?family=Questrial&family=Arimo:wght@400&display=swap">
<style>
  :root {
    --page: #ffffff;
    --card: #d9dadc;
    --teal: #5ec8c6;
    --ink: #000000;
    --pink: #e5197a;
    --white: #ffffff;
    --stitch: rgba(255,255,255,0.6);
  }
  * { box-sizing: border-box; margin: 0; padding: 0; }
  html, body {
    width: 1200px; height: 826px;
    overflow: hidden;
    background: var(--page);
  }
  .range {
    position: relative;
    width: 1200px; height: 826px;
  }
  .pack {
    position: absolute;
    top: 62px;
    width: 338px;
    height: 715px;
  }
  .pack--leather { left: 46px; }
  .pack--leopard { left: 430px; }
  .pack--floral  { left: 815px; }

  .hang-tab {
    position: absolute;
    left: 82px; top: 0;
    width: 164px; height: 82px;
    border-radius: 8px 8px 0 0;
  }
  .hang-tab__slot {
    position: absolute;
    left: 50%; top: 16px;
    transform: translateX(-50%);
    width: 48px; height: 14px;
    border-radius: 7px;
    background: var(--page);
  }
  .pack--leather .hang-tab { background: var(--teal); }
  .pack--leopard .hang-tab,
  .pack--floral .hang-tab { background: var(--ink); }

  .card {
    position: absolute;
    left: 0; top: 79px;
    width: 338px; height: 636px;
    background: var(--card);
    overflow: hidden;
  }
  .product {
    position: absolute;
    inset: 0;
    width: 338px; height: 636px;
  }
  .corner-name {
    position: absolute;
    left: 16px; top: 18px;
    font-family: "Questrial", sans-serif;
    font-size: 22px;
    letter-spacing: 0.5px;
  }
  .pack--leather .corner-name { color: var(--teal); }
  .pack--leopard .corner-name,
  .pack--floral .corner-name { color: var(--pink); }

  .band {
    position: absolute;
    left: 0; top: 323px;
    width: 338px; height: 174px;
    text-align: center;
    padding-top: 30px;
  }
  .pack--leather .band { background: var(--teal); }
  .pack--leopard .band,
  .pack--floral .band { background: var(--ink); }

  .band__name {
    font-family: "Questrial", sans-serif;
    font-size: 44px;
    line-height: 1;
    letter-spacing: 0.5px;
  }
  .pack--leather .band__name { color: var(--white); }
  .pack--leopard .band__name,
  .pack--floral .band__name { color: var(--pink); }

  .band__tagline {
    margin-top: 20px;
    font-family: "Arimo", sans-serif;
    font-size: 17px;
    line-height: 23px;
    color: var(--white);
  }
</style>
</head>
<body>
<main class="range">

  <article class="pack pack--leather">
    <div class="hang-tab"><span class="hang-tab__slot"></span></div>
    <div class="card">
      <svg class="product" viewBox="0 0 338 636" role="img" aria-label="Black pebbled leather brush cover">
        <defs>
          <linearGradient id="leather" x1="0" y1="0" x2="1" y2="1">
            <stop offset="0" stop-color="#3a3a3a"/>
            <stop offset="0.5" stop-color="#1c1c1c"/>
            <stop offset="1" stop-color="#2e2e2e"/>
          </linearGradient>
        </defs>
        <path d="M14,86 Q169,-34 324,86 L258,624 L80,624 Z" fill="url(#leather)"/>
        <path d="M26,92 Q169,-18 312,92 L248,612 L90,612 Z" fill="none" stroke="var(--stitch)" stroke-width="1" stroke-dasharray="3 3"/>
        <path d="M0,0 L338,0 L338,120 L0,330 Z" fill="#ffffff" opacity="0.12"/>
      </svg>
      <span class="corner-name">PlumeSleeve</span>
      <div class="band">
        <h2 class="band__name">PlumeSleeve</h2>
        <p class="band__tagline">Protecting your<br>brushes from grime…<br>one cover at a time</p>
      </div>
    </div>
  </article>

  <article class="pack pack--leopard">
    <div class="hang-tab"><span class="hang-tab__slot"></span></div>
    <div class="card">
      <svg class="product" viewBox="0 0 338 636" role="img" aria-label="Black and white leopard print brush cover">
        <defs>
          <linearGradient id="leopard" x1="0" y1="0" x2="1" y2="1">
            <stop offset="0" stop-color="#8a8a8a"/>
            <stop offset="0.5" stop-color="#5e5e5e"/>
            <stop offset="1" stop-color="#7a7a7a"/>
          </linearGradient>
        </defs>
        <path d="M14,86 Q169,-34 324,86 L258,624 L80,624 Z" fill="url(#leopard)"/>
        <path d="M26,92 Q169,-18 312,92 L248,612 L90,612 Z" fill="none" stroke="var(--stitch)" stroke-width="1" stroke-dasharray="3 3"/>
        <path d="M0,0 L338,0 L338,120 L0,330 Z" fill="#ffffff" opacity="0.12"/>
      </svg>
      <span class="corner-name">PlumeSleeve</span>
      <div class="band">
        <h2 class="band__name">PlumeSleeve</h2>
        <p class="band__tagline">Protecting your<br>brushes from grime…<br>one cover at a time</p>
      </div>
    </div>
  </article>

  <article class="pack pack--floral">
    <div class="hang-tab"><span class="hang-tab__slot"></span></div>
    <div class="card">
      <svg class="product" viewBox="0 0 338 636" role="img" aria-label="Navy brush cover with bright pink, orange and white floral print">
        <defs>
          <linearGradient id="floral" x1="0" y1="0" x2="1" y2="1">
            <stop offset="0" stop-color="#e0609a"/>
            <stop offset="0.45" stop-color="#2b3566"/>
            <stop offset="1" stop-color="#e8703a"/>
          </linearGradient>
        </defs>
        <path d="M14,86 Q169,-34 324,86 L258,624 L80,624 Z" fill="url(#floral)"/>
        <path d="M26,92 Q169,-18 312,92 L248,612 L90,612 Z" fill="none" stroke="var(--stitch)" stroke-width="1" stroke-dasharray="3 3"/>
        <path d="M0,0 L338,0 L338,120 L0,330 Z" fill="#ffffff" opacity="0.12"/>
      </svg>
      <span class="corner-name">PlumeSleeve</span>
      <div class="band">
        <h2 class="band__name">PlumeSleeve</h2>
        <p class="band__tagline">Protecting your<br>brushes from grime…<br>one cover at a time</p>
      </div>
    </div>
  </article>

</main>
</body>
</html>
```